Brivora Collective Business Card Design

We need a business card design for Brivora Collective. We are a healthcare recruiting, wellness and education company. We partner with medical facilities to find quality candidates. We also offer free wellness courses.
The final design should communicate an emphasis on recruiting and wellness
The main purpose of the business card is to utilized it for networking events, give to hospitals, executives, VCs surgery centers and clinics. I want it to be sleek, clean, use of our brand colors and professional.

```html
<!DOCTYPE html>
<html lang="en">
<head>
<meta charset="UTF-8">
<title>Brivora Collective – Business Card</title>
<link rel="stylesheet" href="https://fonts.googleapis.com/css2?family=Josefin+Sans:wght@300;400;600;700&display=swap">
<style>
  :root {
    --stage: #3b3b3d;
    --paper: #ffffff;
    --paper-shade: #f1f1f1;
    --brand-green: #00574d;
    --brand-green-light: #0a6b5f;
    --ink: #3a3a3a;
    --soft-white: #eef3f2;
    --muted-green: #7fa8a2;
  }
  * { box-sizing: border-box; margin: 0; padding: 0; }
  html, body {
    width: 1200px; height: 900px; overflow: hidden;
    background: var(--stage);
    font-family: "Josefin Sans", sans-serif;
  }
  .canvas {
    width: 1200px; height: 900px;
    display: flex; flex-direction: column; align-items: center; justify-content: center;
    gap: 56px;
  }
  .card {
    width: 600px; height: 343px; position: relative; overflow: hidden;
    box-shadow: 0 14px 30px rgba(0,0,0,.35);
  }

  /* Front */
  .card--front {
    background: linear-gradient(135deg, var(--paper) 40%, var(--paper-shade));
  }
  .front__brand {
    position: absolute; left: 0; right: 0; top: 110px;
    display: flex; align-items: center; justify-content: center; gap: 14px;
  }
  .brand-square {
    width: 26px; height: 26px; border-radius: 4px; background: var(--brand-green); flex: none;
  }
  .front__name {
    color: var(--brand-green); font-weight: 600; font-size: 34px; letter-spacing: .5px; line-height: 1;
  }
  .front__rule {
    position: absolute; left: 64px; right: 64px; top: 208px;
    height: 1px; background: var(--brand-green);
  }
  .front__tagline {
    position: absolute; left: 0; right: 0; top: 224px;
    display: flex; justify-content: center; align-items: center; gap: 14px;
    color: var(--ink); font-size: 15px; letter-spacing: 2px; font-weight: 400; line-height: 1;
  }
  .tag-dot { width: 6px; height: 6px; border-radius: 50%; background: var(--brand-green); }

  /* Back */
  .card--back {
    background: linear-gradient(120deg, var(--brand-green-light), var(--brand-green) 55%);
    color: var(--soft-white);
  }
  .back__brand {
    position: absolute; right: 40px; top: 40px;
    display: flex; align-items: center; gap: 14px;
  }
  .back__brand .brand-square { background: var(--soft-white); width: 30px; height: 30px; }
  .back__name { font-size: 36px; font-weight: 400; color: var(--soft-white); line-height: 1; }

  .person {
    position: absolute; left: 40px; right: 40px; top: 172px;
  }
  .person__head {
    display: flex; align-items: center; gap: 14px;
  }
  .person__name {
    font-weight: 700; font-size: 22px; letter-spacing: 1.5px; line-height: 1; white-space: nowrap;
  }
  .person__rule {
    flex: 1; height: 1px; background: var(--muted-green);
  }
  .person__role {
    font-size: 14px; color: var(--muted-green); margin-top: 6px; letter-spacing: .5px; line-height: 1.2;
  }
  .contacts {
    position: absolute; left: 40px; top: 232px; list-style: none;
    display: flex; flex-direction: column; gap: 7px;
  }
  .contact {
    display: flex; align-items: center; gap: 12px; font-size: 15px; letter-spacing: .3px; line-height: 1.2;
  }
  .contact svg { width: 15px; height: 15px; flex: none; }
</style>
</head>
<body>
<main class="canvas">

  <section class="card card--front" aria-label="Card front">
    <div class="front__brand">
      <span class="brand-square" aria-hidden="true"></span>
      <span class="front__name">Brivora Collective</span>
    </div>
    <div class="front__rule"></div>
    <p class="front__tagline">
      <span>RECRUITING</span><span class="tag-dot"></span>
      <span>WELLNESS</span><span class="tag-dot"></span>
      <span>EDUCATION</span>
    </p>
  </section>

  <section class="card card--back" aria-label="Card back">
    <div class="back__brand">
      <span class="brand-square" aria-hidden="true"></span>
      <span class="back__name">Brivora Collective</span>
    </div>

    <div class="person">
      <div class="person__head">
        <p class="person__name">MARISA HOLT</p>
        <span class="person__rule" aria-hidden="true"></span>
      </div>
      <p class="person__role">Co-Founder, CEO</p>
    </div>

    <ul class="contacts">
      <li class="contact">
        <svg viewBox="0 0 24 24" fill="none" stroke="#eef3f2" stroke-width="2"><path d="M5 3h4l2 5-3 2a11 11 0 0 0 6 6l2-3 5 2v4a2 2 0 0 1-2 2A17 17 0 0 1 3 5a2 2 0 0 1 2-2z"/></svg>
        <span>000-000-0000</span>
      </li>
      <li class="contact">
        <svg viewBox="0 0 24 24" fill="none" stroke="#eef3f2" stroke-width="2"><rect x="2" y="5" width="20" height="14" rx="1"/><path d="M2 6l10 7 10-7"/></svg>
        <span>info@brivoracollective.com</span>
      </li>
      <li class="contact">
        <svg viewBox="0 0 24 24" fill="none" stroke="#eef3f2" stroke-width="2"><circle cx="12" cy="12" r="10"/><path d="M2 12h20M12 2c3 3 3 17 0 20M12 2c-3 3-3 17 0 20"/></svg>
        <span>www.brivoracollective.com</span>
      </li>
      <li class="contact">
        <svg viewBox="0 0 24 24" fill="none" stroke="#eef3f2" stroke-width="2"><path d="M12 22s7-7 7-12a7 7 0 0 0-14 0c0 5 7 12 7 12z"/><circle cx="12" cy="10" r="2.5"/></svg>
        <span>Austin, Texas 78701, US</span>
      </li>
    </ul>
  </section>

</main>
</body>
</html>
```